Lucien business card

Business card for commercial photography , photographer specialized in advertising, architecture and interior photography, adventure imagery and camera work. 40 years old, worked for the last 20 years. Business card needs to convey a sense of confidence in work achieved. Card needs to be eye catching as will be left behind in many people's offices. Should also mention discreetly NRVB accredited photographer at the verso of the card. Phone number and website link must be apparent easily.

Target Market(s)

Advertising agencies, commercial photography representation

Industry/Entity Type

Architecture

Contact Information for Business Card

Phone number : +61 470 918 264
lucien.marvaux@velmora.example
www.lucienmarvaux.example

Font styles to use
Sans Serif

Requirements
Must have
• Email adress
• Website
• Phone number
• Name
• Photographer
Nice to have
• NRVB accredited photographer
Should not have
• Rond corners

```html
<!DOCTYPE html>
<html lang="en">
<head>
<meta charset="utf-8">
<title>Lucien business card</title>
<link rel="stylesheet" href="https://fonts.googleapis.com/css2?family=Source+Sans+3:wght@400;600&display=swap">
<style>
  :root {
    --paper: #ffffff;
    --periwinkle: #b4c7e7;
    --ink: #000000;
    --sky-text: #c5d4f0;
    --icon-blue: #8fa6d6;
    --icon-dark: #5b6f9e;
    --muted: #6d7a94;
  }
  * { margin: 0; padding: 0; box-sizing: border-box; }
  html, body {
    width: 1200px; height: 735px; overflow: hidden;
    background: var(--paper);
    font-family: "Source Sans 3", "Myriad Pro", Arial, sans-serif;
  }
  .card { position: relative; width: 1200px; height: 735px; background: var(--paper); }

  .services {
    position: absolute; left: 73px; top: 123px; width: 332px; height: 473px;
    background: var(--periwinkle);
    list-style: none;
    padding: 8px 56px 0 0;
    text-align: right;
    color: var(--paper);
    font-size: 51px; line-height: 64.5px;
  }

  .website {
    position: absolute; left: 357px; top: 185px; width: 787px; height: 88px;
    background: var(--ink);
    color: var(--sky-text);
    font-size: 70px; line-height: 88px;
    padding-left: 16px;
    white-space: nowrap;
  }

  .contact {
    position: absolute; left: 418px;
    display: flex; align-items: center;
    color: var(--ink);
    font-size: 39px;
    white-space: nowrap;
  }
  .contact--email { top: 348px; }
  .contact--phone { top: 438px; }
  .contact .icon { flex: none; }
  .contact--email .label { margin-left: 8px; }
  .contact--phone .label { margin-left: 20px; }
  .contact--phone .icon { margin-left: 11px; }

  .identity {
    position: absolute; left: 420px; top: 548px;
    white-space: nowrap;
    color: var(--ink);
  }
  .identity__name { font-size: 34px; font-weight: 600; line-height: 40px; }
  .identity__role { font-weight: 400; color: var(--icon-dark); }
  .identity__accreditation { font-size: 22px; line-height: 30px; color: var(--muted); margin-top: 4px; }
</style>
</head>
<body>
<main class="card">
  <ul class="services">
    <li>Commercial</li>
    <li>Travel</li>
    <li>People</li>
    <li>Interiors</li>
    <li>Wildlife</li>
    <li>Reportage</li>
    <li>Essays</li>
  </ul>

  <div class="website">lucienmarvaux.example</div>

  <div class="contact contact--email">
    <svg class="icon" width="72" height="72" viewBox="0 0 72 72" aria-hidden="true">
      <defs>
        <linearGradient id="envelope-fill" x1="0" y1="0" x2="0" y2="1">
          <stop offset="0" stop-color="#ffffff"/>
          <stop offset="1" stop-color="#c9d3ea"/>
        </linearGradient>
      </defs>
      <path d="M4 30 L36 6 L68 30 L68 66 L4 66 Z" fill="url(#envelope-fill)" stroke="var(--icon-dark)" stroke-width="3" stroke-linejoin="round"/>
      <path d="M4 30 L36 52 L68 30" fill="none" stroke="var(--icon-dark)" stroke-width="3" stroke-linejoin="round"/>
      <path d="M4 66 L30 46 M68 66 L42 46" fill="none" stroke="var(--icon-dark)" stroke-width="3"/>
      <text x="36" y="36" text-anchor="middle" font-family="Source Sans 3, Arial, sans-serif" font-size="26" fill="#1a1a1a">@</text>
    </svg>
    <span class="label">: lucien . marvaux@velmora.example</span>
  </div>

  <div class="contact contact--phone">
    <svg class="icon" width="48" height="82" viewBox="0 0 48 82" aria-hidden="true">
      <rect x="2" y="2" width="44" height="78" rx="9" fill="var(--icon-blue)" stroke="var(--icon-dark)" stroke-width="2"/>
      <rect x="9" y="10" width="30" height="22" rx="2" fill="#e8eefa"/>
      <g fill="#e8eefa">
        <rect x="9" y="40" width="8" height="6" rx="1"/><rect x="20" y="40" width="8" height="6" rx="1"/><rect x="31" y="40" width="8" height="6" rx="1"/>
        <rect x="9" y="50" width="8" height="6" rx="1"/><rect x="20" y="50" width="8" height="6" rx="1"/><rect x="31" y="50" width="8" height="6" rx="1"/>
        <rect x="9" y="60" width="8" height="6" rx="1"/><rect x="20" y="60" width="8" height="6" rx="1"/><rect x="31" y="60" width="8" height="6" rx="1"/>
      </g>
    </svg>
    <span class="label">: +61 470 918 264</span>
  </div>

  <div class="identity">
    <p class="identity__name">Lucien Marvaux <span class="identity__role">· Photographer</span></p>
    <p class="identity__accreditation">NRVB accredited photographer</p>
  </div>
</main>
</body>
</html>
```